Tamaru Peruvian Cuisine needs a take-out menu

We need a new tri-fold 8.5"x11" take out menu for a Peruvian restaurant based in New Rochelle, NY. We have a vast selections of dishes from appetizers, seafood based dishes, desserts, Peruvian ceviches and more. We have attached the following:

Restaurant information
Pictures of our dishes
Tamaru Logo in pdf format
Menu in word format
Old take out menu for reference only! (our dishes have changed)
Updates

Project Deadline Extended
Reason: Need more time to make final decision.

Industry/Entity Type

Restaurant

```html
<!DOCTYPE html>
<html lang="en">
<head>
<meta charset="utf-8">
<title>Tamaru Peruvian Cuisine – Take-Out Menu</title>
<link href="https://fonts.googleapis.com/css2?family=Roboto+Condensed:wght@400;700;900&family=Pinyon+Script&display=swap" rel="stylesheet">
<style>
:root{
  --stage:#e4e4e4;
  --charcoal:#1d1d1d;
  --charcoal-2:#2c2c2c;
  --brown-dark:#3e170a;
  --brown:#6b3217;
  --brown-light:#8a4622;
  --gold:#e8c64a;
  --cream:#efe6cf;
  --muted:#cfc4a6;
  --red:#8c1d12;
}
*{box-sizing:border-box;margin:0;padding:0}
html,body{width:900px;height:1200px;overflow:hidden;background:var(--stage)}
body{font-family:"Roboto Condensed",sans-serif;color:var(--cream)}
.canvas{position:relative;width:900px;height:1200px}
.sheet{position:absolute;left:80px;width:740px;height:572px;display:flex;box-shadow:0 6px 18px rgba(0,0,0,.25)}
.sheet--outside{top:22px}
.sheet--inside{top:606px}
.panel{width:33.333%;height:100%;padding:14px 14px 10px;position:relative;overflow:hidden}
.panel--dark{background:linear-gradient(90deg,var(--charcoal) 0%,var(--charcoal-2) 50%,var(--charcoal) 100%)}
.panel--brown{background:radial-gradient(ellipse at 50% 40%,var(--brown-light) 0%,var(--brown) 45%,var(--brown-dark) 100%)}
.section-title{font-family:"Pinyon Script",cursive;font-size:24px;color:#fff;text-align:center;line-height:1;margin:6px 0 6px;white-space:nowrap}
.section-title--compact{font-size:21px}
.section-title::before,.section-title::after{content:"";display:inline-block;width:18px;height:1px;background:var(--gold);vertical-align:middle;margin:0 8px}
.item{position:relative;padding-right:44px;margin-bottom:5px}
.item--beside-photo{padding-right:140px}
.item-name{font-weight:700;font-size:9px;color:var(--gold);text-transform:uppercase;letter-spacing:.3px;line-height:1.15}
.item-desc{font-size:7.4px;color:var(--cream);line-height:1.2}
.item-sub{font-size:7.4px;color:var(--gold);line-height:1.2}
.item-price{position:absolute;right:0;top:0;font-size:9px;color:var(--muted)}
.photo{border-radius:8px;box-shadow:0 2px 6px rgba(0,0,0,.5)}
.photo-row{display:flex;gap:8px;margin-bottom:8px}
.sides{position:relative}
.sides-photo{position:absolute;right:46px;top:8px;width:86px;height:62px}
/* cover */
.cover{display:flex;flex-direction:column;align-items:center;text-align:center;padding-top:30px}
.brand{display:flex;align-items:center;gap:8px}
.brand-dot{width:12px;height:12px;border-radius:50%;background:var(--gold)}
.brand-name{font-weight:700;font-size:26px;color:#fff}
.cover-title{margin-top:18px;font-weight:900;font-size:30px;color:#fff;letter-spacing:1px;line-height:1}
.cover-sub{font-size:12px;letter-spacing:3px;color:#fff;margin-top:2px}
.chef-art{width:170px;height:150px;margin-top:12px;border-radius:6px;background:radial-gradient(circle at 50% 55%,#d7b62a 0%,#b3241a 45%,#4a1a0c 80%)}
.address{font-size:9.5px;color:#fff;margin-top:12px}
.phone{display:flex;align-items:center;gap:6px;font-size:22px;color:#fff;font-weight:400;letter-spacing:1px}
.hours{width:100%;margin-top:6px;background:var(--red);padding:5px 4px;font-size:9px;color:var(--gold);line-height:1.3}
.notes{margin-top:6px;font-size:8px;color:var(--cream);line-height:1.3}
.caption{font-family:"Pinyon Script",cursive;font-size:11px;color:#333;position:absolute;right:18px;bottom:6px}
</style>
</head>
<body>
<main class="canvas">

  <section class="sheet sheet--outside">
    <div class="panel panel--dark">
      <div class="photo-row">
        <div class="photo" role="img" aria-label="Photo of ceviche with sweet potato" style="width:104px;height:86px;background:linear-gradient(135deg,#e9e2d6,#c9b08e)"></div>
        <div class="photo" role="img" aria-label="Photo of creamy seafood soup" style="width:104px;height:86px;background:linear-gradient(135deg,#f2d6a6,#e3a85c)"></div>
      </div>
      <div class="item"><div class="item-name">Aeropuerto</div><div class="item-desc">peruvian style fried rice, mixed with noodles, chicken, beef and shrimp –</div><span class="item-price">$ 18.95</span></div>
      <div class="item"><div class="item-name">Arroz Chaufa</div><div class="item-desc">peruvian style fried rice mixed with choice of beef or chicken Carne –</div><div class="item-sub">Pollo – 12.95</div><span class="item-price">$ 14.95</span></div>
      <div class="item"><div class="item-name">Seco de Carne</div><div class="item-desc">beef ribs stew in aji panka sauce, served with rice and Peruvian canario beans –</div><span class="item-price">$ 15.95</span></div>
      <div class="item"><div class="item-name">Aji de Gallina</div><div class="item-desc">shredded chicken in a spicy aji amarillo creamy sauce, hard-boiled egg, olives, potatoes and rice –</div><span class="item-price">$ 11.95</span></div>
      <h2 class="section-title">Seafood</h2>
      <div class="item"><div class="item-name">Pescado a lo Macho</div><div class="item-desc">fried fish fillet topped with seafood in hot yellow pepper sauce, served with rice and yuccas –</div><span class="item-price">$ 19.95</span></div>
      <div class="item"><div class="item-name">Pescado Sudado</div><div class="item-desc">corvina fish stew, in hot yellow pepper, tomatoes, onions, served with yuccas and rice –</div><span class="item-price">$ 16.95</span></div>
      <div class="item"><div class="item-name">Arroz con Mariscos</div><div class="item-desc">peruvian style paella, red rice served with seafood –</div><span class="item-price">$ 17.95</span></div>
      <div class="item"><div class="item-name">Arroz Chaufa</div><div class="item-desc">peruvian style fried rice served with choice of seafood or shrimp Mariscos –</div><div class="item-sub">Camarones – 17.95</div><span class="item-price">$ 17.95</span></div>
      <div class="item"><div class="item-name">Trucha Frita</div><div class="item-desc">deep fried Trout, served with white rice, fried yuccas and salsa criolla –</div><span class="item-price">$ 18.95</span></div>
      <div class="item"><div class="item-name">Jalea</div><div class="item-desc">deep fried mixed seafood and fish, served with fried yuccas Large –</div><div class="item-sub">Small – 17.95</div><span class="item-price">$ 28.95</span></div>
    </div>

    <div class="panel panel--dark">
      <h2 class="section-title">Chicken</h2>
      <div class="item"><div class="item-name">1/4 Pollo</div><div class="item-desc">quarter chicken, served with two sides –</div><span class="item-price">$ 6.50</span></div>
      <div class="item"><div class="item-name">1/2 Pollo</div><div class="item-desc">half chicken, served with two sides –</div><span class="item-price">$ 8.95</span></div>
      <div class="item"><div class="item-name">1 Pollo</div><div class="item-desc">whole chicken, served with two sides –</div><span class="item-price">$ 16.95</span></div>
      <div class="item"><div class="item-name">Pollo Limeño</div><div class="item-desc">whole chicken, served with French fries, avocado salad and yellow rice</div><span class="item-price">$ 20.95</span></div>
      <div class="item"><div class="item-name">Pollo Chalaco</div><div class="item-desc">whole chicken, served with avocado salad, salchipapa and yellow rice</div><span class="item-price">$ 26.95</span></div>
      <div class="item"><div class="item-name">Pollo Tamaru</div><div class="item-desc">whole chicken, served with avocado salad, arroz chaufa (chicken or steak) and salchipapa</div><span class="item-price">$ 30.95</span></div>
      <h2 class="section-title">Desserts</h2>
      <div class="item"><div class="item-name">Crema Volteada</div><div class="item-desc">Peruvian caramel custard –</div><span class="item-price">$ 5.95</span></div>
      <div class="item"><div class="item-name">Tres Lech</div><div class="item-desc">butter cake soaked in three kinds of milk –</div><span class="item-price">$ 5.95</span></div>
      <div class="item"><div class="item-name">Torta Helada</div><div class="item-desc">Sponge cake topped with strawberry jello –</div><span class="item-price">$ 5.95</span></div>
      <div class="item"><div class="item-name">Torta de Chocholate</div><div class="item-desc">Chocolate cake –</div><span class="item-price">$ 5.95</span></div>
      <div class="item"><div class="item-name">Picarones</div><div class="item-desc">Peruvian style sweet potato doughnut covered with syrup –</div><span class="item-price">$ 5.95</span></div>
      <div class="photo-row" style="position:absolute;left:14px;bottom:12px">
        <div class="photo" role="img" aria-label="Photo of empanada with dipping sauce" style="width:104px;height:80px;background:linear-gradient(135deg,#f4efe6,#d9a45a)"></div>
        <div class="photo" role="img" aria-label="Photo of fried chicken pieces" style="width:104px;height:80px;background:linear-gradient(135deg,#f1e7da,#c06a22)"></div>
      </div>
    </div>

    <div class="panel panel--brown cover">
      <div class="brand"><span class="brand-dot"></span><span class="brand-name">Tamaru</span></div>
      <div class="cover-title">AUTHENTIC</div>
      <div class="cover-sub">PERUVIAN CUISINE</div>
      <div class="chef-art" role="img" aria-label="Cartoon chef mascot illustration"></div>
      <div class="address">120 Harbor Ave, Brookvale, NY 10555</div>
      <div class="phone">
        <svg width="18" height="18" viewBox="0 0 24 24" aria-hidden="true"><rect width="24" height="24" rx="4" fill="#e8c64a"/><path d="M7 5l3 3-2 2c1 2 3 4 5 5l2-2 3 3-2 3C10 18 6 14 5 7z" fill="#3e170a"/></svg>
        914-555-0137
      </div>
      <div class="hours">Delivery Hours<br>Mon - Sun | 11:30 am - 10 pm</div>
      <div class="notes">Notes: Deliveries on order of $15 or more. $5 fee for 3 miles or more. Chef's specials on weekends.</div>
    </div>
  </section>

  <section class="sheet sheet--inside">
    <div class="panel panel--brown">
      <h2 class="section-title">Appetizers</h2>
      <div class="item"><div class="item-name">Chicharron de Calamares</div><div class="item-desc">crispy fried calamari served with house tartar sauce and salsa criolla –</div><span class="item-price">$ 12.95</span></div>
      <div class="item"><div class="item-name">Anticucho Carretiller</div><div class="item-desc">choice chicken or cow's heart Peruvian style kebabs, served with Cusco corn and grilled potatoes Corazon –</div><div class="item-sub">Pollo –</div><span class="item-price">$ 15.95</span></div>
      <div class="item"><div class="item-name">Palta Rellena</div><div class="item-desc">peruvian avocado stuffed with choice of chicken or shrimp, marinated in Peruvian spices Camarones –</div><div class="item-sub">Pollo –</div><span class="item-price">$ 15.95</span></div>
      <div class="item"><div class="item-name">Tamal Criollo</div><div class="item-desc">peruvian chicken tamale, served with salsa criolla –</div><span class="item-price">$ 8.95</span></div>
      <div class="item"><div class="item-name">Salchipapa</div><div class="item-desc">french fries mixed with sliced hot dogs –</div><span class="item-price">$ 5.95</span></div>
      <div class="item"><div class="item-name">Papa a la Huancaina</div><div class="item-desc">boiled potatoes, topped with aji amarillo and queso fresco sauce, egg, olives –</div><span class="item-price">$ 9.95</span></div>
      <div class="item"><div class="item-name">Ocopa Arequipeña</div><div class="item-desc">boiled potatoes, topped with huacatay sauce and queso fresco, egg, olives –</div><span class="item-price">$ 8.95</span></div>
      <div class="item"><div class="item-name">Empanada Limeña</div><div class="item-desc">patties stuffed with choice of chicken or beef –</div><span class="item-price">$ 3.95</span></div>
      <div class="item"><div class="item-name">Causa</div><div class="item-desc">cold mashed potato infused with lime juice, pressed into a cake with chicken or shrimp Camarones –</div><span class="item-price">$ 9.95</span></div>
      <div class="item"><div class="item-name">Choritos a la Chalaca</div><div class="item-desc">steamed mussels topped with diced onions, tomatoes, lime juice and Cusco corn –</div><span class="item-price">$ 10.95</span></div>
      <div class="item"><div class="item-name">Piqueo Tamaru</div><div class="item-desc">Dished combined of Chicharron de Calamares, Papa a la Huancaina, Choritos a la Chalaca and Causa</div><span class="item-price">$ 19.95</span></div>
      <div role="img" aria-label="Photo of lomo saltado plate" style="position:absolute;left:0;right:0;bottom:0;height:62px;background:linear-gradient(90deg,#f4f1ec,#b5562a 50%,#f4f1ec)"></div>
      <span class="caption">Lomo Saltado</span>
    </div>

    <div class="panel panel--dark">
      <h2 class="section-title">Salads</h2>
      <div class="item"><div class="item-name">Ensalada de la Casa</div><div class="item-desc">lettuce, tomatoes, yellow peppers and zucchini –</div><span class="item-price">$ 6.95</span></div>
      <div class="item"><div class="item-name">Ensalada Tamaru</div><div class="item-desc">lettuce, tomatoes, cucumbers, red onions, carrots, radish and avocado –</div><span class="item-price">$ 7.95</span></div>
      <div class="item"><div class="item-name">Ensalada Cesar</div><div class="item-desc">romaine lettuce, croutons, parmesan cheese and Tamaru's special sauce –</div><span class="item-price">$ 8.95</span></div>
      <h2 class="section-title">Soups</h2>
      <div class="item"><div class="item-name">Aguadito Limeño</div><div class="item-desc">chicken and vegetable soup mixed with rice and cilantro Large –</div><div class="item-sub">Small –</div><span class="item-price">$ 9.95</span></div>
      <div class="item"><div class="item-name">Sopa a la Minuta</div><div class="item-desc">traditional milk and angel's hair pasta soup, served with beef and eggs –</div><span class="item-price">$ 12.95</span></div>
      <div class="item"><div class="item-name">Caldo de Gallina</div><div class="item-desc">hen broth with noodles, scallion, potatoes and hard-boiled egg –</div><span class="item-price">$ 12.95</span></div>
      <div class="item"><div class="item-name">Chupe de Camarones Arequipeño</div><div class="item-desc">shrimp soup mixed with rice, green peas, Cusco corn, milk, eggs and Peruvian spices –</div><span class="item-price">$ 15.95</span></div>
      <div class="item"><div class="item-name">Parihuela del Puerto</div><div class="item-desc">classic Peruvian seafood soup –</div><span class="item-price">$ 18.95</span></div>
      <h2 class="section-title">Ceviches</h2>
      <div class="item"><div class="item-name">Leche de Tigre</div><div class="item-desc">ceviche marinade in fresh lime juice –</div><span class="item-price">$ 10.95</span></div>
      <div class="item"><div class="item-name">Tiradito en Salsa de Aji Amarillo</div><div class="item-desc">sashimi style fish in yellow pepper sauce and fresh lime juice, with Cusco corn and sweet potatoes –</div><span class="item-price">$ 12.95</span></div>
      <div class="item"><div class="item-name">Piqueo Chalaco</div><div class="item-desc">dish combined of Ceviche de Pescado and Jalea (Fried Seafood) –</div><span class="item-price">$ 24.95</span></div>
      <div class="item"><div class="item-name">Ceviche</div><div class="item-desc">choice of raw fish, mixed seafood, shrimp or octopus, marinated in lime juice with red onions and sweet potatoes Pescado –</div><div class="item-sub">Camaron – 17.95 | Mixto – 17.95 | Camaron con Pulpo – 18.95</div><span class="item-price">$ 15.95</span></div>
    </div>

    <div class="panel panel--brown">
      <h2 class="section-title">Sides</h2>
      <div class="sides">
        <div class="item item--beside-photo"><div class="item-name">Papas Fritas</div><div class="item-desc">french fries –</div><span class="item-price">$ 3.95</span></div>
        <div class="item item--beside-photo"><div class="item-name">Arroz Blanco o Amarillo</div><div class="item-desc">white/yellow rice –</div><span class="item-price">$ 3.95</span></div>
        <div class="item item--beside-photo"><div class="item-name">Frejoles</div><div class="item-desc">peruvian canario beans –</div><span class="item-price">$ 3.95</span></div>
        <div class="item item--beside-photo"><div class="item-name">Maduros</div><div class="item-desc">sweet plantains –</div><span class="item-price">$ 3.95</span></div>
        <div class="item item--beside-photo"><div class="item-name">Tostones</div><div class="item-desc">fried green plantains –</div><span class="item-price">$ 3.95</span></div>
        <div class="item item--beside-photo"><div class="item-name">Yuca Frita</div><div class="item-desc">fried yuccas –</div><span class="item-price">$ 3.95</span></div>
        <div class="photo sides-photo" role="img" aria-label="Photo of grilled meats and rice dishes" style="background:linear-gradient(135deg,#f3efe8,#8a4a2a)"></div>
      </div>
      <h2 class="section-title section-title--compact">Traditional Dishes</h2>
      <div class="item"><div class="item-name">Parrillada Mixta</div><div class="item-desc">dish combined of grilled NY Strip steak, anticuchos, pork chops and sausage –</div><span class="item-price">$ 30.95</span></div>
      <div class="item"><div class="item-name">Churrasco en Salsa de Camarones</div><div class="item-desc">NY strip steak topped with shrimps on hot yellow pepper sauce, served with rice –</div><span class="item-price">$ 20.95</span></div>
      <div class="item"><div class="item-name">Seco Norteño</div><div class="item-desc">slowly cooked lamb stew in aji panka sauce, with rice and Peruvian canario beans –</div><span class="item-price">$ 20.95</span></div>
      <div class="item"><div class="item-name">Seco de Pato Piurano</div><div class="item-desc">slowly cooked duck stew in aji panka sauce, with rice and hard-boiled yuccas –</div><span class="item-price">$ 17.95</span></div>
      <div class="item"><div class="item-name">Tallarines Verdes con Churrasco</div><div class="item-desc">linguine pasta in Peruvian style pesto sauce served with grilled NY Strip steak –</div><span class="item-price">$ 18.95</span></div>
      <div class="item"><div class="item-name">Tacu Tacu</div><div class="item-desc">peruvian canario beans mixed with rice, with NY Strip or wok-seared beef in soy sauce Churrasco –</div><div class="item-sub">Lomo – 15.95</div><span class="item-price">$ 18.95</span></div>
      <div class="item"><div class="item-name">Churrasco a lo Pobre</div><div class="item-desc">NY Strip steak served with fried eggs, sweet plantains, French fries and rice –</div><span class="item-price">$ 19.95</span></div>
      <div class="item"><div class="item-name">Saltado</div><div class="item-desc">wok-seared steak or chicken, mixed with red onions, tomatoes, in soy sauce, with fries and rice Lomo –</div><div class="item-sub">Pollo – 13.95</div><span class="item-price">$ 15.95</span></div>
    </div>
  </section>

</main>
</body>
</html>
```